Lantern Ridge Tile Inc. Business Card

Looking for business card with embossed raised logo print. Logo provided and want it to be most prominent image on card. Color pallet of black, red, white or charcoal gray preferred for brand recognition. Simple contact information on front and list description of services provided on back. Services included....Custom Showers, Tub Surrounds, Backsplashes, Fireplaces, Floors and more. Dustless Demolition, Lifetime Warranty, Proud member of the Federated Stoneworks Trade Guild

Target Market(s)

High end residential remodel work and new home builders

Contact Information for Business Card

Phone # (402) 555-0193 email address, Lanternridgets@mailvane.net Colby Hanswirth Owner

Requirements
Must have
• Business logo as most prominent image on the front of business card. Along with contact information and name Colby Hanswirth. Would like to see services provided on the back of the card.

```html
<!DOCTYPE html>
<html lang="en">
<head>
<meta charset="utf-8">
<title>Lantern Ridge Tile Inc. Business Card</title>
<link rel="stylesheet" href="https://fonts.googleapis.com/css2?family=Montserrat:wght@500;700&family=Arimo:wght@400;700&display=swap">
<style>
  :root {
    --brand-red: #d9232b;
    --brand-red-light: #e03a40;
    --card-white: #ffffff;
    --ink: #1c1c1c;
    --charcoal: #2b2b2b;
    --backdrop: #e9e9e9;
  }
  * { margin: 0; padding: 0; box-sizing: border-box; }
  html, body { width: 1200px; height: 900px; overflow: hidden; }
  body {
    background: var(--backdrop);
    position: relative;
    font-family: "Arimo", Arial, sans-serif;
  }
  .card {
    position: absolute;
    width: 630px;
    height: 360px;
    border-radius: 28px;
    box-shadow: 0 10px 28px rgba(0,0,0,0.22);
    overflow: hidden;
  }
  .wordmark-square { background: currentColor; flex: none; }
  .wordmark-name {
    font-family: "Montserrat", Arial, sans-serif;
    font-weight: 700;
    letter-spacing: 1px;
    text-transform: uppercase;
    line-height: 1.1;
  }

  /* Back of card: services */
  .card-back {
    left: 90px; top: 80px;
    background: linear-gradient(135deg, var(--brand-red) 0%, var(--brand-red) 60%, var(--brand-red-light) 100%);
    color: var(--card-white);
  }
  .card-back .wordmark {
    position: absolute;
    left: 0; right: 0; top: 92px;
    display: flex; align-items: center; justify-content: center; gap: 14px;
  }
  .card-back .wordmark-square { width: 38px; height: 38px; }
  .card-back .wordmark-name { font-size: 34px; white-space: nowrap; }
  .services {
    position: absolute;
    left: 30px; right: 30px; top: 176px;
    text-align: center;
  }
  .services-title {
    font-weight: 700;
    font-size: 20px;
    letter-spacing: 0.5px;
    margin-bottom: 10px;
  }
  .services-list {
    list-style: none;
    font-size: 16px;
    line-height: 1.55;
  }

  /* Front of card: contact */
  .card-front {
    left: 480px; top: 460px;
    background: var(--card-white);
    color: var(--ink);
  }
  .card-front .wordmark {
    position: absolute;
    left: 36px; top: 150px;
    width: 260px;
    display: flex; align-items: center; gap: 12px;
    color: var(--brand-red);
  }
  .card-front .wordmark-square { width: 34px; height: 34px; }
  .card-front .wordmark-name { font-size: 24px; }
  .divider {
    position: absolute;
    left: 314px; top: 110px;
    width: 2px; height: 130px;
    background: var(--charcoal);
  }
  .contact {
    position: absolute;
    left: 334px; top: 118px;
    width: 272px;
  }
  .contact-name {
    font-weight: 700;
    font-size: 22px;
    color: var(--brand-red);
    text-transform: uppercase;
    letter-spacing: 0.3px;
    white-space: nowrap;
  }
  .contact-role { font-size: 17px; margin: 2px 0 14px; }
  .contact-line {
    display: flex; align-items: center; gap: 8px;
    font-size: 16px; margin-top: 6px;
    white-space: nowrap;
  }
  .contact-icon { width: 20px; height: 18px; flex: none; }
</style>
</head>
<body>

<section class="card card-back" aria-label="Card back, services">
  <div class="wordmark">
    <span class="wordmark-square"></span>
    <span class="wordmark-name">Lantern Ridge Tile Inc</span>
  </div>
  <div class="services">
    <h2 class="services-title">SERVICES</h2>
    <ul class="services-list">
      <li>• Custom Showers • Tub Surrounds • Backsplashes • Fireplaces</li>
      <li>• Floors and more • Dustless Demolition • Lifetime Warranty</li>
      <li>• Proud member of the Federated Stoneworks Trade Guild</li>
    </ul>
  </div>
</section>

<section class="card card-front" aria-label="Card front, contact">
  <div class="wordmark">
    <span class="wordmark-square"></span>
    <span class="wordmark-name">Lantern Ridge<br>Tile Inc</span>
  </div>
  <div class="divider"></div>
  <div class="contact">
    <p class="contact-name">Colby Hanswirth</p>
    <p class="contact-role">Owner</p>
    <p class="contact-line">
      <svg class="contact-icon" viewBox="0 0 20 18" aria-hidden="true">
        <rect width="20" height="18" rx="4" fill="var(--brand-red)"/>
        <path d="M6 4c1 0 1.5 2 1.5 2.5S6.5 7.5 6.8 8.3c.6 1.3 1.6 2.3 2.9 2.9.8.3 1.3-.7 1.8-.7S14 11 14 12s-1 2-2.5 2C8 14 4 10 4 6.5 4 5 5 4 6 4z" fill="#fff"/>
      </svg>
      (402) 555-0193
    </p>
    <p class="contact-line">
      <svg class="contact-icon" viewBox="0 0 20 18" aria-hidden="true">
        <rect width="20" height="18" rx="4" fill="var(--brand-red)"/>
        <rect x="4" y="5" width="12" height="8" fill="none" stroke="#fff" stroke-width="1.3"/>
        <path d="M4 5l6 5 6-5" fill="none" stroke="#fff" stroke-width="1.3"/>
      </svg>
      Lanternridgets@mailvane.net
    </p>
  </div>
</section>

</body>
</html>
```